Electrical contractor in San Diego county since 1988

Provide a company name/ logo for business cards and forms. Newer and more modern old card is attached. Color preference is black and orange. Simple and streamlined nothing too busy. I have also attached a card that represents the simplicity of what we are looking for.

Contractor

```html
<!DOCTYPE html>
<html lang="en">
<head>
<meta charset="utf-8">
<title>KM Electric Inc. – Business Card</title>
<link rel="stylesheet" href="https://fonts.googleapis.com/css2?family=Source+Sans+3:ital,wght@0,400;0,600;0,700;1,400&display=swap">
<style>
  :root {
    --ink: #111111;
    --paper: #ffffff;
    --accent: #f07300;
    --band: #000000;
  }
  * { margin: 0; padding: 0; box-sizing: border-box; }
  html, body {
    width: 1200px;
    height: 1000px;
    overflow: hidden;
    background: var(--paper);
    font-family: "Source Sans 3", "Myriad Pro", Arial, sans-serif;
    color: var(--ink);
  }
  .canvas {
    position: relative;
    width: 1200px;
    height: 1000px;
  }
  .card {
    position: absolute;
    left: 75px;
    top: 200px;
    width: 1054px;
    height: 604px;
    border: 3px solid var(--band);
    background: var(--paper);
    overflow: hidden;
  }
  .brand {
    position: absolute;
    left: 35px;
    top: 44px;
    width: 420px;
  }
  .brand-mark {
    display: block;
    width: 64px;
    height: 64px;
    background: var(--accent);
    margin-bottom: 20px;
  }
  .brand-name {
    font-weight: 700;
    font-size: 76px;
    line-height: 0.95;
    color: var(--ink);
    letter-spacing: -0.5px;
  }
  .license {
    position: absolute;
    left: 35px;
    top: 376px;
    font-size: 25px;
    font-weight: 400;
  }
  .services {
    position: absolute;
    right: 50px;
    top: 50px;
    font-size: 38px;
    font-weight: 700;
    white-space: nowrap;
  }
  .services .divider,
  .person .divider {
    display: inline-block;
    width: 3px;
    background: var(--accent);
    vertical-align: middle;
  }
  .services .divider { height: 40px; margin: 0 10px; position: relative; top: -3px; }
  .services .amp { font-weight: 400; }
  .contact {
    position: absolute;
    right: 50px;
    top: 150px;
    text-align: right;
    line-height: 1.1;
  }
  .contact .phone { font-size: 44px; font-weight: 700; }
  .contact .fax { font-size: 44px; font-weight: 400; }
  .contact .fax strong { font-weight: 700; }
  .address {
    position: absolute;
    right: 50px;
    top: 312px;
    text-align: right;
    font-size: 34px;
    font-weight: 400;
    line-height: 1.32;
  }
  .accent-rule {
    position: absolute;
    left: 0;
    right: 0;
    top: 429px;
    height: 14px;
    background: var(--accent);
  }
  .name-band {
    position: absolute;
    left: 0;
    right: 0;
    top: 443px;
    bottom: 0;
    background: var(--band);
  }
  .person {
    position: absolute;
    left: 42px;
    top: 40px;
    color: var(--paper);
    white-space: nowrap;
    font-size: 64px;
    line-height: 1;
  }
  .person .name { font-weight: 700; }
  .person .divider { height: 60px; margin: 0 14px 0 16px; position: relative; top: -4px; }
  .person .title { font-style: italic; font-weight: 400; font-size: 60px; }
</style>
</head>
<body>
<div class="canvas">
  <div class="card">
    <div class="brand">
      <span class="brand-mark"></span>
      <div class="brand-name">KM Electric<br>Inc.</div>
    </div>
    <div class="license">Lic. 604218</div>

    <div class="services">Commerial<span class="divider"></span>New <span class="amp">&amp;</span> Remodel</div>

    <div class="contact">
      <div class="phone">619.555.0142</div>
      <div class="fax">Fax: <strong>555.0187</strong></div>
    </div>

    <div class="address">
      <div>PO Box 2417</div>
      <div>Pine Hollow, CA 92011-0420</div>
    </div>

    <div class="accent-rule"></div>
    <div class="name-band">
      <div class="person"><span class="name">Dalton Hayes</span><span class="divider"></span><span class="title">President</span></div>
    </div>
  </div>
</div>
</body>
</html>
```